Rock, Paper Scissors Championship Flyer

We need a dynamic, bold and exciting flyer to promote the following event at our sports center. The event will be primarily focused for adults, but children are welcome to join

Rock, Paper, Scissors Championship - $$$ prizes
Date: June 9th, 2018
Time: 11am-4pm
Fee: $2 to enter, free for spectators
Heats to determine the overall ‘Rock, Paper, Scissors’ champion!
- Cash prizes on offer
- Live music.
- Food and beverage available for purchase

Belvorrow Sports Center, Harwick Vale
908-555-3162
www.belvorrowgrounds.example

Must include our logo (does not have to be huge) and County seal (both attached)

Colors

Designer to choose colors to be used in the design.

Requirements
Must have
• Should be fun and colorful
• The following info and attached logos:
• Rock, Paper, Scissors Championship - $$$ prizes
• Date: June 9th, 2018
• Time: 11am-4pm
• Fee: $2 to enter, free for spectators
• Heats to determine the overall ‘Rock, Paper, Scissors’ champion!
• - Cash prizes on offer
• - Live music.
• - Food and beverage available for purchase
• Belvorrow Sports Center, Harwick Vale
• 908-555-3162
• www.belvorrowgrounds.example
Nice to have
• There are a few inspirational photos attached to give an idea of what we are looking for.

```html
<!DOCTYPE html>
<html lang="en">
<head>
<meta charset="utf-8">
<title>Rock Paper Scissors Championship – Belvorrow Sports Center</title>
<link rel="stylesheet" href="https://fonts.googleapis.com/css2?family=Bowlby+One&family=Roboto+Condensed:wght@700&family=Montserrat:wght@600;700&display=swap">
<style>
  :root {
    --navy: #123763;
    --navy-deep: #0d2a4f;
    --blue: #1d4f86;
    --teal: #3f86a6;
    --backdrop: #a8a8a8;
    --paper: #f4f3f1;
    --white: #ffffff;
    --seal: #c99a3a;
  }
  * { margin: 0; padding: 0; box-sizing: border-box; }
  html, body { width: 1200px; height: 2190px; overflow: hidden; }
  body { background: var(--backdrop); position: relative; }

  .flyer {
    position: absolute; left: 80px; top: 358px;
    width: 1040px; height: 1474px;
    background: var(--paper); overflow: hidden;
    box-shadow: 0 6px 18px rgba(0,0,0,.35);
    font-family: "Roboto Condensed", sans-serif;
    font-weight: 700;
    color: var(--navy);
  }
  .crowd-photo {
    position: absolute; left: 0; top: 150px; width: 1040px; height: 1150px;
    background: linear-gradient(100deg, #e9e2dc 0%, #f7f6f4 25%, #e4e3e6 50%, #f6f5f3 72%, #e6e7ea 100%);
  }
  .top-band { position: absolute; left: 0; top: 0; width: 1040px; height: 320px; }
  .brand {
    position: absolute; left: 50px; top: 40px; width: 170px;
    text-align: center; color: var(--white);
    font-size: 22px; line-height: 1.15; letter-spacing: 1px;
  }
  .brand-dot { width: 46px; height: 46px; border-radius: 50%; background: var(--white); margin: 0 auto 12px; }
  .seal { position: absolute; right: 54px; top: 24px; width: 134px; height: 134px; border-radius: 50%; background: var(--seal); }

  .title {
    position: absolute; left: 0; width: 1040px; top: 186px;
    text-align: center; font-family: "Bowlby One", sans-serif; font-weight: 400;
    font-size: 60px; line-height: 78px; color: var(--navy);
  }
  .hands {
    position: absolute; left: 310px; top: 440px; width: 400px; height: 370px;
    background: radial-gradient(ellipse at center, rgba(29,79,134,.55), rgba(29,79,134,.15) 70%, transparent);
    border-radius: 40px;
  }
  .date { position: absolute; left: 52px; top: 476px; font-size: 60px; line-height: 66px; }
  .time { position: absolute; left: 52px; top: 676px; font-size: 30px; line-height: 40px; }
  .fee { position: absolute; right: 56px; top: 480px; text-align: right; }
  .fee-label { font-size: 46px; line-height: 52px; }
  .fee-amount { font-size: 118px; line-height: 116px; }
  .fee-free { font-size: 42px; line-height: 46px; margin-top: 20px; }
  .fee-note { font-size: 28px; line-height: 32px; }
  .championship {
    position: absolute; left: 0; width: 1040px; top: 808px; text-align: center;
    font-family: "Bowlby One", sans-serif; font-weight: 400; font-size: 56px; line-height: 90px;
  }
  .prize-band {
    position: absolute; left: 0; top: 914px; width: 1040px; height: 102px;
    background: var(--navy); color: var(--white);
    font-family: "Montserrat", sans-serif; font-weight: 700; font-size: 56px;
    display: flex; align-items: center; justify-content: center;
  }
  .highlights {
    position: absolute; left: 0; width: 1040px; top: 1040px; list-style: none;
    text-align: center; font-family: "Montserrat", sans-serif; font-weight: 600;
    font-size: 34px; line-height: 45px;
  }
  .treeline {
    position: absolute; left: 0; top: 1160px; width: 1040px; height: 160px;
    background: linear-gradient(180deg, rgba(63,134,166,0) 0%, rgba(63,134,166,.7) 35%, var(--blue) 70%, var(--navy-deep) 100%);
  }
  .footer {
    position: absolute; left: 0; top: 1310px; width: 1040px; height: 164px;
    background: var(--navy-deep);
  }
  .contact {
    position: absolute; left: 0; top: 1274px; width: 1040px; list-style: none;
    text-align: center; color: var(--white);
    font-family: "Montserrat", sans-serif; font-weight: 700; font-size: 22px; line-height: 28px;
  }
  .contact li { margin-bottom: 10px; }
  .contact svg { display: block; margin: 0 auto 6px; width: 16px; height: 16px; }
</style>
</head>
<body>
  <main class="flyer">
    <div class="crowd-photo" role="img" aria-label="Faded photo of a group of people stacking hands together"></div>

    <svg class="top-band" viewBox="0 0 1040 320" aria-hidden="true">
      <path fill="var(--navy)" d="M0 0H1040V262L1010 250 990 230 1000 205 975 190 940 200 915 180 880 150 850 165 820 140 780 155 740 130 700 150 660 135 620 160 590 140 550 150 520 135 480 155 440 140 400 160 370 150 330 170 300 160 270 185 240 178 220 200 190 210 170 240 140 232 110 258 80 250 50 268 20 262 0 275Z"/>
    </svg>

    <div class="brand"><div class="brand-dot"></div>BELVORROW SPORTS CENTER</div>
    <div class="seal" aria-hidden="true"></div>

    <h1 class="title">ROCK<br>PAPER<br>SCISSORS</h1>
    <div class="hands" role="img" aria-label="Rock, paper and scissors hand icons"></div>

    <p class="date">June 9th,<br>2018</p>
    <p class="time">Time:<br>11am-4pm</p>

    <div class="fee">
      <p class="fee-label">Entry Fee:</p>
      <p class="fee-amount">$2</p>
      <p class="fee-free">FREE for</p>
      <p class="fee-note">SPECTATORS</p>
    </div>

    <h2 class="championship">CHAMPIONSHIP</h2>
    <div class="prize-band">$$$ prizes</div>

    <ul class="highlights">
      <li>Cash prizes on offer</li>
      <li>Live music.</li>
      <li>Food and beverage available for purchase</li>
    </ul>

    <div class="treeline" role="img" aria-label="Blue pine forest silhouette"></div>
    <div class="footer"></div>

    <ul class="contact">
      <li>
        <svg viewBox="0 0 16 16"><path fill="#fff" d="M8 1a5 5 0 0 0-5 5c0 4 5 9 5 9s5-5 5-9a5 5 0 0 0-5-5zm0 7a2 2 0 1 1 0-4 2 2 0 0 1 0 4z"/></svg>
        Belvorrow Sports Center, Harwick Vale
      </li>
      <li>
        <svg viewBox="0 0 16 16"><path fill="#fff" d="M4 1l2.5 3-1.5 2a8 8 0 0 0 5 5l2-1.5 3 2.5-1.5 2.5C8 15 1 8 1.5 2.5z"/></svg>
        908-555-3162
      </li>
      <li>
        <svg viewBox="0 0 16 16" fill="none" stroke="#fff" stroke-width="1.3"><circle cx="8" cy="8" r="6.5"/><ellipse cx="8" cy="8" rx="3" ry="6.5"/><path d="M1.5 8h13"/></svg>
        www.belvorrowgrounds.example
      </li>
    </ul>
  </main>
</body>
</html>
```